New Business Card for chocolate Company

I am looking to have business cards for my Chocolate Company Velvet Spoon Sweets.
I hand make all organic, fair trade, vegan, gluten free, allergy friendly chocolate. We are located in Austin Texas and are very Proud to be a locally made good. I have my logo and new sticker design for our boxes but now I need cards. I was thinking either natural craft or white. But I want to have a bit of funk to the cards so someone will hold onto it for a long time.
The important info is
Dora Pennweather
Owner and Chocolatier
Velvet Spoon Sweets
velvetspoonsweetsatx.example
velvetspoonsweets@mailbox.example
velvetspoonsweets on instagram
512.555.0183

Velvet Spoon sweets are Vegan ,Gluten free, organic, fair trade, allergy friendly hand made chocolate.

Target Market(s)

We cater to all ages. Our chocolate is on the higher price scale and is a decadent treat. But we make custom molds for any event kids party's to an elegant wedding.

Industry/Entity Type

Business

Requirements
Must have
• Good design logo and some sort of austin vibe.

```html
<!DOCTYPE html>
<html lang="en">
<head>
<meta charset="utf-8">
<title>Velvet Spoon Sweets — Business Card</title>
<link rel="stylesheet" href="https://fonts.googleapis.com/css2?family=Josefin+Sans:wght@300;400;600;700&display=swap">
<style>
  :root {
    --backdrop: #77726e;
    --card: #f8f8f6;
    --gold: #9a8551;
    --ink: #3b3a38;
    --ink-soft: #5a5956;
  }
  html, body {
    margin: 0;
    padding: 0;
    width: 799px;
    height: 1200px;
    overflow: hidden;
    background: var(--backdrop);
  }
  .canvas {
    position: relative;
    width: 799px;
    height: 1200px;
    font-family: "Josefin Sans", sans-serif;
  }
  .card {
    position: absolute;
    background: var(--card);
  }
  .card--contact {
    left: 96px;
    top: 388px;
    width: 258px;
    height: 423px;
  }
  .card--brand {
    left: 449px;
    top: 380px;
    width: 271px;
    height: 440px;
  }
  .rule {
    position: absolute;
    left: 25px;
    width: 208px;
    height: 0;
    border-top: 1.5px solid var(--gold);
  }
  .rule--top { top: 69px; }
  .rule--bottom { top: 355px; }

  .text-line {
    position: absolute;
    left: 0;
    right: 0;
    margin: 0;
    text-align: center;
    white-space: nowrap;
  }
  .owner-name {
    top: 121px;
    font-size: 13px;
    font-weight: 600;
    letter-spacing: 2.2px;
    text-transform: uppercase;
    color: var(--ink);
  }
  .owner-role {
    top: 148px;
    font-size: 10px;
    font-weight: 600;
    letter-spacing: 1.8px;
    text-transform: uppercase;
    color: var(--gold);
  }
  .contact-line {
    font-size: 10px;
    font-weight: 300;
    letter-spacing: 1px;
    color: var(--ink-soft);
  }
  .contact-line--company { top: 209px; }
  .contact-line--phone { top: 232px; }
  .contact-line--email { top: 254px; letter-spacing: 0.6px; }
  .contact-line--social { top: 275px; }
  .contact-line--web { top: 298px; letter-spacing: 0.6px; }

  .brand-name {
    position: absolute;
    left: 0;
    right: 0;
    top: 150px;
    margin: 0;
    text-align: center;
    color: var(--gold);
    font-size: 30px;
    font-weight: 700;
    letter-spacing: 1.5px;
    line-height: 1.25;
    text-transform: uppercase;
  }

  .tagline {
    font-size: 9px;
    font-weight: 700;
    letter-spacing: 1.2px;
    color: var(--gold);
  }
  .tagline--one { top: 336px; }
  .tagline--two { top: 358px; }
  .tagline--three { top: 379px; }
</style>
</head>
<body>
<main class="canvas">
  <section class="card card--contact" aria-label="Contact side">
    <div class="rule rule--top"></div>

    <p class="text-line owner-name">Dora Pennweather</p>
    <p class="text-line owner-role">Owner and Chocolatier</p>

    <p class="text-line contact-line contact-line--company">Velvet Spoon Sweets</p>
    <p class="text-line contact-line contact-line--phone">512.555.0183</p>
    <p class="text-line contact-line contact-line--email">velvetspoonsweets@mailbox.example</p>
    <p class="text-line contact-line contact-line--social">velvetspoonsweets on instagram</p>
    <p class="text-line contact-line contact-line--web">velvetspoonsweetsatx.example</p>

    <div class="rule rule--bottom"></div>
  </section>

  <section class="card card--brand" aria-label="Brand side">
    <h1 class="brand-name">Velvet Spoon<br>Sweets</h1>
    <p class="text-line tagline tagline--one">Vegan | Gluten free</p>
    <p class="text-line tagline tagline--two">organic | fair trade,</p>
    <p class="text-line tagline tagline--three">allergy friendly hand made chocolate</p>
  </section>
</main>
</body>
</html>
```